Business card design incorporating discount offer

We are a trade services company and we need a double sided business card that is going to be used by our tradesmen to give to customers on completion of their jobs.

Below are the key elements of the card that we would like to include:

-Main logo with text 'Corvane Building Aid' underneath.
-Up to 12 smaller icon logos with text 'Your local all-trade experts' to emphasise the point that we cover all the trades
-Discount offer - 10% discount
-Telephone number and website address
-Blank space for tradesman to enter his/her name
-Request for customer feedback with feedback url

This business card will be printed on regular card. In the past we have favoured designs that use a black background but we're open to new ideas.

I have attached a few files:

-A simple wire frame example to show how this card could look with the different elements mentioned above, feel free to use a layout similar to this or come up with something totally different (biz-card.pdf)
-Front and back of a loyalty card the we've used in the past (this card was printed on plastic)
-Front and back of a key fob design that we've previously used (this card was printed on plastic)
-A logo file with the 12 small icons and the main logo image

If you need further images or information please ask.

```html
<!DOCTYPE html>
<html lang="en">
<head>
<meta charset="utf-8">
<title>Corvane Building Aid – Business Card</title>
<link href="https://fonts.googleapis.com/css2?family=Arimo:wght@400;700&family=Montserrat:wght@700;800&display=swap" rel="stylesheet">
<style>
  :root {
    --backdrop: #a7a9ac;
    --brand-blue: #2b80c4;
    --brand-grey: #8a8c8f;
    --card-white: #ffffff;
    --tile-brown: #b9834f;
    --tile-purple: #a54a9c;
    --tile-ochre: #d9a12f;
    --tile-slate: #6c7a87;
    --tile-grey: #9a9c9e;
    --tile-sky: #1f9be0;
    --tile-yellow: #f1cf3a;
    --tile-teal: #2fb2b0;
    --tile-red: #e0393e;
    --tile-green: #79b948;
  }
  * { margin: 0; padding: 0; box-sizing: border-box; }
  html, body { width: 1200px; height: 999px; overflow: hidden; }
  body {
    background: var(--backdrop);
    position: relative;
    font-family: "Arimo", Arial, sans-serif;
  }
  .card {
    position: absolute;
    width: 650px;
    height: 420px;
    background: var(--card-white);
    display: flex;
    box-shadow: 0 10px 24px rgba(0,0,0,0.25);
  }
  /* Front */
  .card-front { left: 80px; top: 85px; }
  .front-identity {
    flex: 1;
    padding: 110px 0 0 78px;
    position: relative;
  }
  .brand-name {
    font-weight: 700;
    font-size: 54px;
    color: var(--brand-grey);
    letter-spacing: 1px;
  }
  .brand-tagline {
    margin-top: 30px;
    font-weight: 700;
    font-size: 29px;
    color: var(--brand-grey);
  }
  .contact-list {
    position: absolute;
    left: 82px;
    bottom: 62px;
    list-style: none;
  }
  .contact-item {
    display: flex;
    align-items: center;
    gap: 6px;
    font-weight: 700;
    font-size: 26px;
    color: var(--brand-grey);
    line-height: 33px;
  }
  .contact-icon {
    width: 28px;
    height: 26px;
    background: var(--brand-blue);
    display: flex;
    align-items: center;
    justify-content: center;
  }
  .offer-panel {
    width: 192px;
    background: var(--brand-blue);
    color: var(--card-white);
    padding: 95px 0 0 0;
    text-align: center;
    position: relative;
  }
  .offer-figure {
    font-family: "Montserrat", Arial, sans-serif;
    font-weight: 800;
    font-size: 92px;
    line-height: 90px;
    position: relative;
    display: inline-block;
  }
  .offer-figure sup {
    position: absolute;
    top: -8px;
    right: -30px;
    font-size: 34px;
    line-height: 34px;
  }
  .offer-label {
    font-family: "Montserrat", Arial, sans-serif;
    font-weight: 700;
    font-size: 24px;
    margin-top: 10px;
  }
  .offer-sub { font-size: 21px; }
  .offer-note {
    position: absolute;
    left: 36px;
    bottom: 40px;
    text-align: left;
    font-size: 15px;
    line-height: 18px;
  }
  /* Back */
  .card-back { left: 440px; top: 532px; }
  .trade-strip {
    width: 205px;
    padding: 52px 0 0 37px;
    display: grid;
    grid-template-columns: 60px 60px;
    grid-auto-rows: 60px;
    gap: 11px 16px;
  }
  .trade-tile {
    border-radius: 8px;
    box-shadow: inset 0 -4px 0 rgba(0,0,0,0.18);
  }
  .back-panel {
    flex: 1;
    background: var(--brand-blue);
    color: var(--card-white);
    padding: 30px 0 0 10px;
  }
  .back-heading {
    font-weight: 700;
    font-size: 24px;
    display: flex;
    align-items: center;
    gap: 8px;
  }
  .tradesman-label {
    margin: 58px 0 0 32px;
    font-size: 19px;
  }
  .tradesman-field {
    margin: 6px 0 0 30px;
    width: 372px;
    height: 82px;
    background: var(--card-white);
  }
  .feedback-heading {
    margin: 48px 0 0 30px;
    font-weight: 700;
    font-size: 19px;
  }
  .feedback-text {
    margin: 38px 0 0 30px;
    font-size: 19px;
    line-height: 22px;
  }
  .feedback-url { font-weight: 700; }
</style>
</head>
<body>
  <section class="card card-front">
    <div class="front-identity">
      <div class="brand-name">Corvane</div>
      <div class="brand-tagline">Corvane Building Aid</div>
      <ul class="contact-list">
        <li class="contact-item">
          <span class="contact-icon">
            <svg width="18" height="18" viewBox="0 0 24 24"><path fill="#fff" d="M6.6 10.8a15.1 15.1 0 0 0 6.6 6.6l2.2-2.2c.3-.3.7-.4 1-.2 1.1.4 2.3.6 3.6.6.6 0 1 .4 1 1V20c0 .6-.4 1-1 1A17 17 0 0 1 3 4c0-.6.4-1 1-1h3.5c.6 0 1 .4 1 1 0 1.3.2 2.5.6 3.6.1.3 0 .7-.2 1z"/></svg>
          </span>
          0800 555 0142
        </li>
        <li class="contact-item">
          <span class="contact-icon">
            <svg width="18" height="18" viewBox="0 0 24 24" fill="none" stroke="#fff" stroke-width="1.8"><circle cx="12" cy="12" r="9"/><ellipse cx="12" cy="12" rx="4" ry="9"/><line x1="3" y1="12" x2="21" y2="12"/></svg>
          </span>
          corvane-aid.co.uk
        </li>
      </ul>
    </div>
    <div class="offer-panel">
      <div class="offer-figure">10<sup>%</sup></div>
      <div class="offer-label">DISCOUNT</div>
      <div class="offer-sub">with this card</div>
      <div class="offer-note">Check our website for<br>full Offer Details</div>
    </div>
  </section>

  <section class="card card-back">
    <div class="trade-strip">
      <div class="trade-tile" style="background:var(--tile-brown)" role="img" aria-label="Carpentry trade icon"></div>
      <div class="trade-tile" style="background:var(--tile-purple)" role="img" aria-label="Bathroom trade icon"></div>
      <div class="trade-tile" style="background:var(--tile-ochre)" role="img" aria-label="Joinery trade icon"></div>
      <div class="trade-tile" style="background:var(--tile-slate)" role="img" aria-label="Plumbing trade icon"></div>
      <div class="trade-tile" style="background:var(--tile-grey)" role="img" aria-label="Electrical trade icon"></div>
      <div class="trade-tile" style="background:var(--tile-sky)" role="img" aria-label="Gas trade icon"></div>
      <div class="trade-tile" style="background:var(--tile-yellow)" role="img" aria-label="Plastering trade icon"></div>
      <div class="trade-tile" style="background:var(--tile-teal)" role="img" aria-label="Appliance trade icon"></div>
      <div class="trade-tile" style="background:var(--tile-red)" role="img" aria-label="Decorating trade icon"></div>
      <div class="trade-tile" style="background:var(--tile-green)" role="img" aria-label="Pest control trade icon"></div>
    </div>
    <div class="back-panel">
      <h2 class="back-heading">
        <svg width="18" height="14" viewBox="0 0 18 14"><path fill="#fff" d="M8 0 0 7l8 7V10L4 7l4-3zM17 0 9 7l8 7V10l-4-3 4-3z"/></svg>
        Your Local All-Trade Experts
      </h2>
      <p class="tradesman-label">Your Corvane Tradesman:</p>
      <div class="tradesman-field"></div>
      <p class="feedback-heading">What Do You Think of Our Services?</p>
      <p class="feedback-text">Please leave your feedback online:<br><span class="feedback-url">www.corvane-aid.co.uk/feedback</span></p>
    </div>
  </section>
</body>
</html>
```